International tradind company needs a professional Business Card

We are an international trading company and we need a business card for our CEO and employers so they can give it away in their meetings and while networking.
We want the card design quality to cause an immediate "wow" and we count on you to do that!

key-words and concepts to communicate: trustworthiness, ethics, sucess, modern, global business, networking

Our favorite colours are blue and grey but we are open to suggestions.

It would be recommended that our logo was part of the card. You can see it in www.kovendagroup.com . We also would like the following info on the card:
Name
position in the company
cell phone and personal email

```html
<!DOCTYPE html>
<html lang="en">
<head>
<meta charset="utf-8">
<title>Kovenda Group – Business Card</title>
<link href="https://fonts.googleapis.com/css2?family=Questrial&display=swap" rel="stylesheet">
<style>
  :root {
    --backdrop: #d9d9d6;
    --card: #ffffff;
    --brand-navy: #1f1456;
    --brand-blue: #2f5fb3;
    --tagline-blue: #3a7cc4;
    --ink: #1c1c1c;
    --rule: #8a8a8a;
  }
  * { margin: 0; padding: 0; box-sizing: border-box; }
  html, body {
    width: 1200px;
    height: 900px;
    overflow: hidden;
    background: var(--backdrop);
    font-family: "Questrial", sans-serif;
    color: var(--ink);
  }
  .canvas { position: relative; width: 1200px; height: 900px; }
  .card {
    position: absolute;
    top: 148px;
    width: 375px;
    height: 640px;
    background: var(--card);
    border-radius: 18px;
    box-shadow: 0 2px 8px rgba(0,0,0,0.18);
    overflow: hidden;
  }
  .card--front { left: 195px; }
  .card--back { left: 648px; }

  .brand {
    position: absolute;
    display: flex;
    align-items: center;
    gap: 23px;
  }
  .brand__mark {
    width: 100px;
    height: 100px;
    border-radius: 50%;
    background: var(--brand-blue);
    flex: none;
  }
  .brand__text { display: flex; flex-direction: column; }
  .brand__name {
    font-size: 28px;
    line-height: 32px;
    color: var(--brand-navy);
    white-space: nowrap;
  }
  .brand__tagline {
    font-size: 18px;
    line-height: 22px;
    color: var(--tagline-blue);
    white-space: nowrap;
  }
  .card--front .brand { left: 25px; top: 495px; }
  .card--back .brand { left: 25px; top: 43px; }

  .contact {
    position: absolute;
    left: 0;
    width: 100%;
    text-align: center;
    font-size: 15px;
    line-height: 21px;
  }
  .person { top: 278px; }
  .person__name { font-size: 17px; font-weight: bold; letter-spacing: 0.3px; }
  .person__role { margin-bottom: 20px; }
  .divider {
    position: absolute;
    top: 456px;
    left: 72px;
    width: 232px;
    border: 0;
    border-top: 1px solid var(--rule);
  }
  .office { top: 476px; }
  .office p + p.gap { margin-top: 20px; }
</style>
</head>
<body>
<main class="canvas">
  <section class="card card--front" aria-label="Card front">
    <div class="brand">
      <span class="brand__mark" aria-hidden="true"></span>
      <div class="brand__text">
        <span class="brand__name">Kovenda Group</span>
        <span class="brand__tagline">Business Services</span>
      </div>
    </div>
  </section>

  <section class="card card--back" aria-label="Card back">
    <div class="brand">
      <span class="brand__mark" aria-hidden="true"></span>
      <div class="brand__text">
        <span class="brand__name">Kovenda Group</span>
        <span class="brand__tagline">Business Services</span>
      </div>
    </div>

    <div class="contact person">
      <p class="person__name">Marco Tavel</p>
      <p class="person__role">CEO</p>
      <p>+351 912000457</p>
      <p>marco@kovendagroup.com</p>
    </div>

    <hr class="divider">

    <div class="contact office">
      <p>Rua das Flores, 28, 2o Esq</p>
      <p>1200-195 Lisboa</p>
      <p class="gap">T: +351 210000318</p>
      <p class="gap">contact@kovendagroup.com</p>
      <p>www.kovendagroup.com</p>
    </div>
  </section>
</main>
</body>
</html>
```